Email Marketing Campaign Templates

Email drip childcare campaign designed to communicate with parents interested in services. We would like the template(s) to be created so that we can change the content as needed.I will add below collateral that we have used in the past as well as logo.
three to for templates 1.) welcome template 2/ things to bring 3) generic template
Target Market(s)
Parents and Millennials
Industry/Entity Type
Childcare
Colors
85cae6
0493ce
9bcb3c
add136
fefefe
faa54b
cadf82
86cae7
33a6d7
Requirements
Must have
- Photos of staff with children
Nice to have
- Photos

```html
<!DOCTYPE html>
<html lang="en">
<head>
<meta charset="utf-8">
<title>Bloomwood Early Education Center</title>
<link href="https://fonts.googleapis.com/css2?family=Dosis:wght@300;400;500&family=Exo+2:wght@300;400&family=Comfortaa:wght@700&display=swap" rel="stylesheet">
<style>
  :root{
    --backdrop:#e4e4e4;
    --sky:#c6e7f6;
    --blue:#41aee3;
    --pink:#e5127f;
    --green:#74b42d;
    --yellow:#f7be1c;
    --orange:#f55a17;
    --mustard:#e5c832;
    --white:#fefefe;
    --ink:#4a4a4a;
  }
  *{box-sizing:border-box;margin:0;padding:0}
  html,body{width:1200px;height:1200px;overflow:hidden;background:var(--backdrop)}
  .stage{position:absolute;left:0;top:0;width:1500px;height:1500px;transform:scale(.8);transform-origin:0 0}
  .flyer{position:absolute;left:412px;top:38px;width:676px;height:1424px;background:var(--sky);overflow:hidden}
  .abs{position:absolute}
  .photo{position:absolute}

  .brand-panel{left:0;top:7px;width:148px;height:260px;background:var(--white)}
  .brand-name{position:absolute;left:18px;top:66px;width:124px;display:flex;align-items:center;gap:6px;font:400 20px/1 'Dosis',sans-serif;color:var(--green);white-space:nowrap}
  .brand-dot{flex:none;width:18px;height:18px;border-radius:50%;background:var(--green)}
  .brand-title{position:absolute;left:29px;top:124px;font:300 21px/24px 'Dosis',sans-serif;color:var(--ink);letter-spacing:.3px}

  .waves-top{position:absolute;left:0;top:0}

  .callout{position:absolute;top:324px;height:154px;background:var(--yellow);border:3px solid var(--white);border-radius:16px;display:flex;align-items:center;justify-content:center;text-align:center;font:300 18px/23px 'Dosis',sans-serif;color:var(--white);text-transform:uppercase;padding:0 10px}
  .callout.lead{font-size:23px;line-height:29px;font-weight:400;padding:0 6px}

  .stat{position:absolute;left:0;width:208px;display:flex;flex-direction:column;align-items:center;justify-content:center;color:var(--white);font:700 11px/1 'Comfortaa',sans-serif;text-transform:uppercase;letter-spacing:.3px}
  .stat .num{font:400 36px/1 'Comfortaa',sans-serif;margin:8px 0 10px}
  .stat.pink{top:502px;height:95px;background:var(--pink)}
  .stat.yellow{top:632px;height:97px;background:var(--yellow)}
  .stat.orange{top:768px;height:95px;background:var(--orange)}

  .philosophy-head{position:absolute;left:356px;top:498px;width:320px;height:61px;background:var(--blue);color:var(--white);font:300 35px/61px 'Exo 2',sans-serif;padding-left:18px}
  .philosophy-body{position:absolute;left:356px;top:570px;width:311px;font:300 12.6px/14.4px 'Exo 2',sans-serif;color:var(--ink);text-align:justify}
  .philosophy-body p{margin-bottom:14px}

  .info-bar{position:absolute;left:0;top:1107px;width:676px;height:70px;background:var(--green);color:var(--white)}
  .hours{position:absolute;left:89px;top:9px;font:300 15px/18px 'Dosis',sans-serif}
  .site{position:absolute;left:399px;top:20px;font:400 21px/1 'Dosis',sans-serif;letter-spacing:.3px}

  .location{position:absolute;left:0;top:1177px;width:676px;height:225px;background:var(--mustard)}
  .map{position:absolute;left:81px;top:0;width:507px;height:225px;background:linear-gradient(135deg,#e9eef2,#d6e6f0)}
  .address-card{position:absolute;left:240px;top:22px;width:186px;height:46px;background:var(--white);border-radius:3px;font:400 15px/18px 'Dosis',sans-serif;color:#111;text-align:center;padding-top:5px;box-shadow:0 1px 3px rgba(0,0,0,.25)}
  .pin{position:absolute;left:244px;top:76px}
  .footer-strip{position:absolute;left:0;top:1402px;width:676px;height:22px;background:var(--green)}
</style>
</head>
<body>
<div class="stage">
  <div class="flyer">
    <div class="photo" role="img" aria-label="Two young girls doing a paper craft at a classroom table" style="left:156px;top:7px;width:520px;height:280px;background:linear-gradient(135deg,#e7d7b4,#c9a27a 55%,#8f6a5a)"></div>

    <div class="abs brand-panel">
      <div class="brand-name"><span class="brand-dot"></span>Bloomwood</div>
      <div class="brand-title">BLOOMWOOD<br>EARLY<br>EDUCATION<br>CENTER</div>
    </div>

    <svg class="waves-top" width="676" height="520" viewBox="0 0 676 520">
      <path d="M0 228 C120 278 240 302 380 282 C500 264 600 220 676 155 L676 300 L0 300 Z" fill="var(--pink)"/>
      <path d="M0 264 C150 312 300 322 440 302 C540 290 620 264 676 242 L676 300 C560 320 420 330 300 318 L80 500 L0 500 Z" fill="var(--green)"/>
    </svg>

    <div class="callout lead" style="left:16px;width:154px">It’s always a beautiful day at Bloomwood!</div>
    <div class="callout" style="left:182px;width:152px">Our open environment fosters autonomy &amp; community.</div>
    <div class="callout" style="left:346px;width:152px">From an early age, children learn by seeing, doing, and helping their friends.</div>
    <div class="callout" style="left:509px;width:152px">Our outdoor environment encourages imaginative group play.</div>

    <div class="stat pink">We have<span class="num">4</span>Magical classrooms</div>
    <div class="photo" role="img" aria-label="Bright classroom with green walls and small tables" style="left:209px;top:502px;width:108px;height:95px;background:linear-gradient(160deg,#b5cf46,#d9c9a8 60%,#9a6e6e)"></div>
    <div class="stat yellow">Staffed with<span class="num">8</span>Amazing teachers</div>
    <div class="photo" role="img" aria-label="Teacher reading a book with a toddler" style="left:209px;top:632px;width:108px;height:97px;background:linear-gradient(140deg,#9ccf3c,#e8d9c4 55%,#5a7fc1)"></div>
    <div class="stat orange">And<span class="num">8</span>Open spots</div>
    <div class="photo" role="img" aria-label="Outdoor playground with slides and shade umbrellas" style="left:209px;top:768px;width:108px;height:95px;background:linear-gradient(180deg,#bcd6e8,#8a9a8c 45%,#c8b8a4)"></div>

    <div class="philosophy-head">OUR PHILOSOPHY</div>
    <div class="philosophy-body">
      <p>Bloomwood Early Education Center creates the ideal environment for kids to feel safe, loved, and accepted as they try new ideas, develop academic skills and imitate adult roles. We learn through play and believe that play makes it possible for children to learn social skills and develop friendships.</p>
      <p>Exploring, discovering, questioning, and guessing–these are all important activities that engage young children. When children play, they become active decision-makers in their own scenarios. Bloomwood Early Education Center promotes the development of the whole child through play.</p>
      <p>Our intimate, nurturing environment is well suited for working in both small and large groups, as well as individually, to manipulate, solve problems, and interact. At the end of the day, we know that children are adept knowledge builders who apply what they’ve learned to different situations. We believe this is their foundation for the future.</p>
    </div>

    <div class="photo" role="img" aria-label="Young girl typing on a laptop" style="left:0;top:917px;width:225px;height:190px;background:linear-gradient(135deg,#e9a46a,#b5582e 60%,#5a3a36)"></div>
    <div class="photo" role="img" aria-label="Child playing an acoustic guitar" style="left:225px;top:917px;width:226px;height:190px;background:linear-gradient(135deg,#c97a2c,#e8a04a 50%,#7a4a22)"></div>
    <div class="photo" role="img" aria-label="Smiling boy reading in a library" style="left:451px;top:917px;width:225px;height:190px;background:linear-gradient(135deg,#8e7d5e,#cbb69a 50%,#3e4a5c)"></div>
    <svg class="abs" style="left:0;top:895px" width="676" height="110" viewBox="0 0 676 110">
      <path d="M0 15 C200 -5 420 0 676 25 L676 100 C600 60 520 30 451 35 C400 25 300 15 225 25 C120 30 40 70 0 100 Z" fill="var(--pink)"/>
      <path d="M0 0 L676 0 L676 25 C420 0 200 -5 0 15 Z" fill="var(--sky)"/>
    </svg>

    <div class="info-bar">
      <div class="hours">Hours:<br>Monday – Friday : 7:00 a.m. – 6:00 p.m.<br>Phone: 614-555-0142.</div>
      <div class="site">www.bloomwood4kids.com</div>
    </div>

    <div class="location">
      <div class="map" role="img" aria-label="Street map of the city centre showing the center's location"></div>
      <div class="address-card">228 Maple Grove Street<br>Fairview, Ohio 43200</div>
      <svg class="pin" width="22" height="30" viewBox="0 0 22 30" aria-hidden="true">
        <path d="M11 0C5 0 0 5 0 11c0 8 11 19 11 19s11-11 11-19C22 5 17 0 11 0z" fill="#e53935"/>
        <circle cx="11" cy="11" r="4" fill="#8e1b1b"/>
      </svg>
    </div>
    <div class="footer-strip"></div>
  </div>
</div>
</body>
</html>
```